Manufacturing company needs new business card.

I need a unique Business Card that will truly stand out. Nothing too busy. Simple is good, right? Not looking for a standard design either. No cookie cutter layout. I am just looking for something interesting and a bit different. Does't have to completely off the wall crazy, just not your run of the mill business card. Clean and modern with a touch of industrial.

Target Market(s)

Air conditioning industry, Architects, builders.

Industry/Entity Type

Business

Contact Information for Business Card

Details to be included on card are:

Peter Vance
Managing Director

T: 1300 847 519
M: 0428 593 174
W: www.brenvaleworks.com.au
E: peter.vance@brenvaleworks.com.au
A: 58 Harwick Lane, Sydney NSW 2000

Font styles to use
Sans Serif

Colors
0355a3
848484
fbfbfb

Requirements
Must have
• Card design must be landscape.

```html
<!DOCTYPE html>
<html lang="en">
<head>
<meta charset="utf-8">
<title>Brenvale Works – Business Card</title>
<link href="https://fonts.googleapis.com/css2?family=Open+Sans:wght@400;600&display=swap" rel="stylesheet">
<style>
  :root {
    --brand-blue: #0355a3;
    --brand-grey: #848484;
    --card-white: #fbfbfb;
    --ink: #2e2e2e;
    --rule: #b9b9b9;
    --stage-top: #8aa6c8;
    --stage-bottom: #6f8bb4;
  }
  * { margin: 0; padding: 0; box-sizing: border-box; }
  html, body { width: 1200px; height: 1000px; overflow: hidden; }
  body {
    background: linear-gradient(160deg, var(--stage-top), var(--stage-bottom));
    font-family: "Open Sans", Arial, sans-serif;
    display: flex;
    flex-direction: column;
    align-items: center;
    justify-content: center;
    gap: 60px;
  }
  .card {
    width: 630px;
    height: 360px;
    position: relative;
    box-shadow: 0 10px 30px rgba(30, 45, 75, 0.35);
  }
  /* Front */
  .card--front { background: var(--card-white); }
  .front__brand {
    position: absolute;
    left: 48px;
    top: 92px;
    display: flex;
    align-items: center;
    gap: 10px;
  }
  .brand__square {
    width: 22px; height: 22px;
    background: var(--brand-blue);
  }
  .front__brand .brand__name {
    color: var(--brand-blue);
    font-weight: 600;
    font-size: 22px;
    letter-spacing: -0.2px;
  }
  .front__rule-h {
    position: absolute;
    left: 48px; top: 172px;
    width: 252px; height: 1px;
    background: var(--rule);
  }
  .front__rule-v {
    position: absolute;
    left: 300px; top: 92px;
    width: 1px; height: 81px;
    background: var(--rule);
  }
  .person {
    position: absolute;
    left: 322px; top: 96px;
  }
  .person__name {
    color: var(--brand-blue);
    font-size: 27px;
    font-weight: 400;
    letter-spacing: 0.5px;
    line-height: 1.1;
  }
  .person__role {
    color: var(--brand-grey);
    font-size: 17px;
    line-height: 1.4;
  }
  .contacts {
    position: absolute;
    left: 300px; top: 196px;
    list-style: none;
  }
  .contacts li {
    display: flex;
    align-items: center;
    gap: 10px;
    height: 24px;
    color: var(--ink);
    font-size: 15px;
  }
  .contacts__key {
    width: 16px; height: 16px;
    background: var(--brand-grey);
    color: var(--card-white);
    font-size: 10px;
    font-weight: 600;
    display: flex;
    align-items: center;
    justify-content: center;
    flex: none;
  }
  /* Back */
  .card--back {
    background: linear-gradient(135deg, #8c8c8c, var(--brand-grey) 55%, #767676);
    display: flex;
    align-items: center;
    justify-content: center;
  }
  .back__brand {
    display: flex;
    align-items: center;
    gap: 16px;
  }
  .back__brand .brand__square {
    width: 40px; height: 40px;
    background: var(--card-white);
  }
  .back__brand .brand__name {
    color: var(--card-white);
    font-weight: 600;
    font-size: 40px;
    letter-spacing: -0.3px;
  }
</style>
</head>
<body>
  <section class="card card--front" aria-label="Business card front">
    <div class="front__brand">
      <span class="brand__square"></span>
      <span class="brand__name">Brenvale Works</span>
    </div>
    <div class="front__rule-h"></div>
    <div class="front__rule-v"></div>
    <div class="person">
      <h1 class="person__name">PETER VANCE</h1>
      <p class="person__role">Managing Director</p>
    </div>
    <ul class="contacts">
      <li><span class="contacts__key">T</span>1300 847 519</li>
      <li><span class="contacts__key">M</span>0428 593 174</li>
      <li><span class="contacts__key">W</span>www.brenvaleworks.com.au</li>
      <li><span class="contacts__key">E</span>peter.vance@brenvaleworks.com.au</li>
      <li><span class="contacts__key">A</span>58 Harwick Lane, Sydney NSW 2000</li>
    </ul>
  </section>

  <section class="card card--back" aria-label="Business card back">
    <div class="back__brand">
      <span class="brand__square"></span>
      <span class="brand__name">Brenvale Works</span>
    </div>
  </section>
</body>
</html>
```